Bref créative
Brochures for sophisticated nutrition products
Velvet Crest Products
The brochures to be designed should come across richly textured, for someone who likes elite, high quality, luxury products. We will be printing the brochures using foil inks and foil stamped ink, to bring out the colors. There are 6 brochures needed (6 different products). The brochure should bring out the vivid colors of the products themselves as well. When someone holds these brochures in their hands the though that should come to mind is "This must be expensive, high quality products" Please reference files of what the products look like.
Salon & Spa
The target audience is anyone looking to be fit, healthy, happy.
I am open to new ideas on the layouts of brochures, I would consider tri-fold, double folded. 8.5 x 14 should be the size of the brochures.
This is the current layout and feel of the website. You can see the colors of the products here. To get the details of what the content should be, please visit www.qlorbamerica.example and go to the products section. The content there is what we need to use for the brochures.
file 2
file 3
file 4
file 5
Company Logo File
Label for Product called: SOLO chocolate. The bottle color to go on the brochure is black, like the KVR product bottles.
Label for Product called: SOLO vanilla. The bottle color to go on the brochure is black, like the KVR product bottles.
Product called: HoTaru. Additional to this Box are the individual packets that go into it, which will be uploaded in another file.
Product called: HoTaru (Packets).
Image for Product called: KVR.
Image for product called: Flare
Image for product called: PQL
Supplement Facts Content for all products and Brochures
KVR Brochure Content
Flare Brochure Content
SOLO Brochure Content
HoTaru Brochure Content
PQL Brochure Content

```html
<!DOCTYPE html>
<html lang="en">
<head>
<meta charset="utf-8">
<title>Nuvana Flare Brochure</title>
<link href="https://fonts.googleapis.com/css2?family=Open+Sans:wght@400;600;700&display=swap" rel="stylesheet">
<style>
  :root {
    --ink: #0b0b0b;
    --paper: #ffffff;
    --lime: #9ccb3b;
    --teal: #5cc6dc;
    --body: #e9e9e9;
    --muted: #bdbdbd;
    --rule: #111111;
  }
  html, body { margin: 0; padding: 0; overflow: hidden; background: var(--ink); }
  .brochure {
    position: relative; width: 1200px; height: 745px; overflow: hidden;
    background: var(--ink);
    font-family: "Open Sans", Arial, sans-serif; color: var(--body);
  }
  .athlete-photo {
    position: absolute; inset: 0;
    background:
      radial-gradient(ellipse 340px 260px at 600px 640px, rgba(150,150,150,.55), rgba(60,60,60,.25) 55%, transparent 80%),
      radial-gradient(ellipse 700px 200px at 560px 560px, rgba(90,90,90,.35), transparent 75%),
      linear-gradient(180deg, #050505 0%, #0d0d0d 60%, #1a1a1a 100%);
  }
  .column { position: absolute; top: 22px; }
  .column--intro { left: 26px; width: 360px; }
  .column--science { left: 432px; width: 350px; }
  h2 { color: var(--lime); font-weight: 700; font-size: 19px; line-height: 1.15; margin: 0 0 14px; }
  p { font-size: 12.5px; line-height: 1.4; margin: 0 0 16px; }
  .claim { font-weight: 600; color: var(--lime); font-size: 12.5px; margin: 0 0 22px; }
  .claim span { color: var(--paper); }
  .column--intro h2.spaced { margin-top: 30px; }
  .blend { color: var(--lime); font-weight: 600; font-size: 12.5px; line-height: 1.35; margin: 0 0 28px; }
  .facts {
    position: absolute; left: 798px; top: 12px; width: 378px;
    background: var(--paper); color: var(--rule);
    font-size: 9.5px; line-height: 1.3; box-sizing: border-box;
    border: 1px solid var(--rule); padding: 4px 6px;
  }
  .facts h3 { font-size: 15px; margin: 0; font-weight: 700; }
  .facts .bar { border-bottom: 5px solid var(--rule); padding-bottom: 2px; }
  .facts .row { display: flex; justify-content: space-between; border-bottom: 1px solid var(--rule); padding: 2px 0; }
  .facts .row b { font-weight: 700; }
  .facts .sub { padding-left: 6px; font-style: italic; }
  .facts .thick { border-bottom: 3px solid var(--rule); }
  .facts .note { padding-top: 2px; }
  .closing { position: absolute; right: 24px; top: 565px; text-align: right; }
  .closing h1 { font-size: 25px; font-weight: 400; color: var(--paper); margin: 0 0 2px; }
  .closing p { color: var(--teal); font-size: 15px; line-height: 1.3; margin: 0; }
</style>
</head>
<body>
<div class="brochure">
  <div class="athlete-photo" role="img" aria-label="Photograph of a muscular athlete seen from behind, arms outstretched, on a dark background"></div>

  <section class="column column--intro">
    <h2>Flare fat, tone up, feel great</h2>
    <p>When running laps and counting calories isn't enough, naturally boost your calorie burning with the Nuvana Flare Dietary Supplement. While exercising regularly and eating a sensible diet are key to any weight management plan, your body needs the occasional boost to be able to achieve maximum results and performance.</p>
    <p class="claim">THE PROBLEM <span>is obesity becoming a leading cause of death</span></p>
    <p class="claim">THE COMPETITION <span>is full of promise, lacking in results</span></p>
    <p class="claim">THE SOLUTION <span>is what you have been looking for</span></p>
    <h2 class="spaced">Commitment to Quality and Excellence</h2>
    <p>We use only the highest quality and purest form of every ingredient manufactured in FDA-inspected facilities to maximize your results. For optimal benefit, combine with other Nuvana products.</p>
    <p>This product is manufactured in a cGMP compliant facility regulated by the FDA.</p>
    <p>This product is not intended to diagnose, treat, cure, mitigate or prevent any disease or medical condition. These statements have not been evaluated by the Food &amp; Drug Administration.</p>
  </section>

  <section class="column column--science">
    <h2>Science behind nature</h2>
    <p>The synergistic ingredients of the Nuvana Flare allows for maximum results, especially when combined with the Nuvana KVR and Nuvana PQL.</p>
    <p class="blend">Thermogenic Fat Burning (Breakdown of stored fat) and Lean Muscle Blend</p>
    <p class="blend">Appetite Suppressant Blend</p>
    <p class="blend">Thyroid Support Blend</p>
    <p class="blend">Anti-oxidant Energy Blend</p>
    <p class="blend">Glycemic Control and Blood Sugar Balancing</p>
    <p class="blend">Carb Blocker</p>
  </section>

  <aside class="facts">
    <div class="bar">
      <h3>Supplement Facts</h3>
      <div>Serving Size: 1 Capsule</div>
      <div>Servings per container: 60</div>
    </div>
    <div class="row thick"><b>Amount Per Serving</b><b>% Daily Value</b></div>
    <div class="row"><div><b>Appetite Control, Blood Sugar Balancing, Thermogenic Fat Burn and Lean Muscle Blend</b><div class="sub">Coleus forskohlii root extract, Garcinia cambogia fruit extract, Black pepper extract, Guarana seed extract</div></div><b>300 mg&nbsp;*</b></div>
    <div class="row"><div><b>Alpha-Amylase Inhibitor</b><div class="sub">White Kidney Bean (Phaseolus vulgaris) extract</div></div><b>150 mg&nbsp;*</b></div>
    <div class="row"><div><b>Anti-oxidant Energy Blend</b><div class="sub">Green Tea catechins (Camellia sinensis)<br>Acetyl L-carnitine</div></div><b>75 mg&nbsp;*</b></div>
    <div class="row thick"><b>Chromium picolinate</b><b>25 mcg&nbsp;&nbsp;2%</b></div>
    <div class="note">*Daily Value not established</div>
    <div class="note">Other Ingredients: Non-GMO Rice Flour, Non-porcine Gelatin Capsule, FD&amp;C Red #40</div>
  </aside>

  <div class="closing">
    <h1>Health and Wellness</h1>
    <p>What makes this trend the fastest growing<br>industry in the world of today?</p>
  </div>
</div>
</body>
</html>
```